BrightHarbor Web Design Project

BrightHarbor IT solutions, a IT mananaged services company is looking to redesign current website (brightharborsolutions.example).

The website should convey professionalism within the managed it services community. The layout should invite users to explore other areas of the site. Should contain tools and other current information that clients or potential clients would find useful. Product pages, special offers and informational pages should be easily editable by non-programmers. Tidewardnet.example is a good site to review as an example of the design components we like.

Target Market(s)

Professional services companies with 10-100 users

Industry/Entity Type

It Company

Requirements
Must have
• • Clickable icons and graphics are good
• SEO - Wordpress could be a great platform for us to work from as we already have internal experience with it and it’s easy to update. If not Wordpress, we would need something that is easy to SEO optimize
• An “our team” section with pictures
• Sell the message to potential clients why they need managed services
• Home page needs to convey our core services at a glance
• Home page needs to load quickly
• Screenshots of our monitoring and security reports
• Easy for us to update/edit certain areas
o New products
o Testimonials
Nice to have
• • Something like TN’s savings calculator - http://www.tidewardnet.example/it-savings-calculator/
• Webform to enter service ticket requests
• Motion of home page banner
• Maybe pull in RSS feeds from current tech news sources
• Rotating content on all pages to keep it fresh
• “Harbor-up” feature for monthly promos
Should not have
• • Should not be overly "techie" in feel.
• Not overly wordy (like current site)

```html
<!DOCTYPE html>
<html lang="en">
<head>
<meta charset="utf-8">
<title>BrightHarbor IT Solutions</title>
<link href="https://fonts.googleapis.com/css2?family=Fira+Sans+Extra+Condensed:wght@400;500;700&family=Arimo:wght@400&display=swap" rel="stylesheet">
<style>
:root{
  --sky-deep:#2a73c8;
  --sky-mid:#7fb0e0;
  --sky-light:#e6f0f9;
  --white:#ffffff;
  --nav-bg:rgba(22,82,125,.9);
  --lime:#9be62a;
  --green:#6fb22a;
  --hero-fill:#b9d5e6;
  --caption-bg:rgba(22,60,40,.85);
  --ink:#222222;
  --body:#555555;
  --muted:#777777;
  --band-top:#e4e4e4;
  --red:#b3151b;
  --olive:#7aa53a;
  --violet:#8a6fc9;
  --gold:#c9a023;
  --footer-top:#4a4a4a;
  --footer-bottom:#151515;
  --footer-text:#8a8a8a;
  --condensed:"Fira Sans Extra Condensed",sans-serif;
}
*{margin:0;padding:0;box-sizing:border-box}
html,body{width:1200px;height:1050px;overflow:hidden}
body{position:relative;font-family:"Arimo",Arial,sans-serif;background:var(--white)}
.sky{position:absolute;left:0;top:0;width:1200px;height:680px;
  background:linear-gradient(100deg,var(--sky-light) 0%,var(--sky-mid) 60%,var(--sky-deep) 100%);}
.sky::after{content:"";position:absolute;left:0;right:0;bottom:0;height:170px;background:linear-gradient(to bottom,rgba(255,255,255,0),#fff 60%)}
.brand{position:absolute;left:150px;top:80px;display:flex;align-items:center;gap:8px;
  font-family:var(--condensed);font-weight:500;font-size:28px;color:var(--green)}
.brand .dot{width:22px;height:22px;border-radius:50%;background:var(--green)}
.contact{position:absolute;right:154px;top:35px;font-family:var(--condensed);font-weight:500;color:#fff;font-size:17px;text-align:right;line-height:22px}
.contact .sep{margin:0 12px}
.remote{display:block;margin-top:10px;color:var(--lime)}
.nav{position:absolute;left:657px;top:107px;width:394px;height:54px;background:var(--nav-bg);
  font-family:var(--condensed);font-weight:500;font-size:20px}
.nav a{color:#fff;text-decoration:none;position:absolute;top:14px}
.hero{position:absolute;left:128px;top:191px;width:930px;height:338px;background:#fff;padding:5px 4px 3px 4px;
  box-shadow:0 8px 14px rgba(0,0,0,.35)}
.hero-art{position:relative;width:922px;height:330px;background:var(--hero-fill)}
.caption{position:absolute;left:0;bottom:0;width:100%;height:80px;background:var(--caption-bg);
  padding:15px 18px;font-family:var(--condensed);font-weight:500;color:#fff;font-size:18px;line-height:27px}
.intro{position:absolute;left:130px;top:560px;width:924px}
.intro h1{font-family:var(--condensed);font-weight:500;font-size:20px;line-height:24px;color:var(--ink);margin-bottom:10px}
.intro p{font-size:12px;line-height:18.5px;color:var(--body);text-align:justify;letter-spacing:-.1px}
.services{position:absolute;left:0;top:678px;width:1200px;height:232px;background:linear-gradient(to bottom,var(--band-top),#fff 90%)}
.service{position:absolute;top:2px;width:212px;border-top:3px solid;padding-top:10px}
.service h2{font-family:var(--condensed);font-weight:500;font-size:20px;line-height:24px;margin:0 0 14px 3px;white-space:nowrap}
.service p{font-size:12px;line-height:19px;color:var(--body);text-align:justify;height:96px;hyphens:auto;-webkit-hyphens:auto;letter-spacing:-.1px}
.service a{display:block;margin-top:2px;margin-left:2px;font-size:12px;color:var(--muted);text-decoration:none}
.s1{left:126px;border-color:#e2b5b5}.s1 h2{color:var(--red)}
.s2{left:355px;border-color:#cde0b5}.s2 h2{color:var(--olive)}
.s3{left:596px;border-color:#c9bde6}.s3 h2{color:var(--violet)}
.s4{left:826px;border-color:#e6cfa0}.s4 h2{color:var(--gold)}
.s1 p{width:213px}.s2 p{width:211px}.s3 p{width:206px}.s4 p{width:206px}
.footer{position:absolute;left:0;top:910px;width:1200px;height:140px;border-top:5px solid #8a8a8a;
  background:radial-gradient(ellipse 400px 90px at 600px 0,var(--footer-top),rgba(0,0,0,0)),linear-gradient(to bottom,#2e2e2e,var(--footer-bottom))}
.footer-brand{position:absolute;left:118px;top:46px;font-family:var(--condensed);font-weight:500;font-size:22px;color:var(--footer-text)}
.copyright{position:absolute;left:258px;top:52px;font-size:12px;color:var(--footer-text)}
.footer-nav a{position:absolute;font-size:12px;color:var(--footer-text);text-decoration:none}
</style>
</head>
<body>
<div class="sky" role="img" aria-label="Bright blue sky with soft white clouds"></div>

<header>
  <div class="brand"><span class="dot"></span>BrightHarbor</div>
  <div class="contact">Toll Free: (888) 555-0142<span class="sep">|</span>Phone: (480) 555-0176
    <span class="remote">Remote Support</span></div>
  <nav class="nav">
    <a href="#" style="left:37px">Home</a>
    <a href="#" style="left:111px">Solutions</a>
    <a href="#" style="left:212px">About Us</a>
    <a href="#" style="left:311px">Contact</a>
  </nav>
</header>

<section class="hero">
  <div class="hero-art" role="img" aria-label="Banner photo: green grass against a blue sky">
    <div class="caption">Every&nbsp; Company&nbsp; Needs to Grow to Survive<br>We Make sure your Technology is Ready for that grouth when you are.</div>
  </div>
</section>

<section class="intro">
  <h1>BrightHarbor can help your business harness the power of new technology, making your business fast and efficient.</h1>
  <p>In the information age of today, one must stay abreast of current technology in order to thrive. New advancements are made daily in dispersing information and collaborative computing. High-speed networks aid in the exchange of electronic information between businesses, their customers, vendors, and peers. Businesses that are quick to act and effectively implement this technology will rise to the top.</p>
</section>

<section class="services">
  <article class="service s1"><h2>IT Consulting Services</h2>
    <p>Insure that your existing system receives quality service. BrightHarbor will troubleshoot problems, install new software or parts, and keep your system in optimal condition...</p><a href="#">More info</a></article>
  <article class="service s2"><h2>IT Service Programs</h2>
    <p>The certified professionals at BrightHarbor will even set up remote access for staff who work outside of the office, but need access to information at their offices...</p><a href="#">More info</a></article>
  <article class="service s3"><h2>Security Vulnerability Scan</h2>
    <p>Assessment services provide critical information about your system hardware and software....</p><a href="#" style="margin-left:7px">More info</a></article>
  <article class="service s4"><h2>Data Backup and Recovery</h2>
    <p>Standalone systems, workstations, network servers, notebooks, peripherals, replacement parts, upgrades, software, Network Design &amp; Installation -</p><a href="#">More info</a></article>
</section>

<footer class="footer">
  <div class="footer-brand">BrightHarbor</div>
  <div class="copyright">Copyright 2012 All rights Reserved.</div>
  <nav class="footer-nav">
    <a href="#" style="left:774px;top:44px">Home</a>
    <a href="#" style="left:832px;top:44px">Solutions</a>
    <a href="#" style="left:909px;top:44px">About Us</a>
    <a href="#" style="left:991px;top:44px">Contact</a>
    <a href="#" style="left:926px;top:75px">Careers</a>
    <a href="#" style="left:989px;top:75px">SiteMap</a>
  </nav>
</footer>
</body>
</html>
```